Tarnwick Youth Harbor Centers
Gala Invitation
"Opening the Door"
We seek a design for our annual fundraising ball invitation to be held on November 3, 2012. We are a private foundation that operates multiple Youth Harbor Center sites within the city of Chicago.
We would like to see an elegant design, befitting a formal event, but with a modern and sleek tone. We envision black and silver tones, possibly juxtaposed with colorful photos of smiling children. However, we are not married to any one particular design concept or color palette.
While our tagline, "Opening the Door" certainly lends itself to many design posibilities, we would like to see creative and subtle, rather than more obvious interpretations.
For further background on the Youth Harbor Centers Federation, see www.yhcfed-example.org.
This invitation will be sent to our foundation members and prospective guests.
We need an invitation and a matching "save the date card".

```html
<!DOCTYPE html>
<html lang="en">
<head>
<meta charset="utf-8">
<title>Tarnwick Youth Harbor Centers – 35th Annual Benefit Gala</title>
<link rel="stylesheet" href="https://fonts.googleapis.com/css2?family=Questrial&display=swap">
<style>
  :root {
    --page: #ffffff;
    --night: #050608;
    --harbor-blue: #2f8fd6;
    --bright-blue: #4aa6e6;
    --numeral-dark: #15171a;
    --paper-white: #f2f4f6;
    --label: #222;
  }
  * { margin: 0; padding: 0; box-sizing: border-box; }
  html, body {
    width: 1200px; height: 802px; overflow: hidden;
    background: var(--page);
    font-family: "Questrial", "Century Gothic", sans-serif;
  }
  .sheet { position: relative; width: 1200px; height: 802px; }

  .streaks {
    background:
      linear-gradient(90deg,
        transparent 0%, rgba(47,143,214,.18) 6%, transparent 9%,
        rgba(47,143,214,.35) 14%, transparent 17%,
        rgba(47,143,214,.22) 24%, transparent 27%,
        rgba(74,166,230,.55) 36%, rgba(47,143,214,.2) 40%, transparent 44%,
        rgba(74,166,230,.45) 50%, rgba(47,143,214,.6) 54%, transparent 58%,
        rgba(47,143,214,.3) 64%, transparent 68%,
        rgba(74,166,230,.5) 74%, transparent 78%,
        rgba(47,143,214,.25) 86%, transparent 90%,
        rgba(47,143,214,.15) 96%, transparent 100%),
      linear-gradient(180deg, #0b1f33 0%, var(--night) 55%, #0a1a2a 100%);
  }

  .placeholder-figure {
    position: absolute;
    background: linear-gradient(180deg, var(--bright-blue), var(--harbor-blue));
    border-radius: 6px;
    opacity: .85;
  }

  /* Envelope back */
  .envelope {
    position: absolute; left: 48px; top: 12px;
    width: 590px; height: 720px; overflow: hidden;
  }
  .envelope .flap { position: absolute; left: 0; top: 0; width: 590px; height: 350px; }
  .envelope .numeral {
    position: absolute; right: 38px; top: -62px;
    font-size: 250px; line-height: 1; letter-spacing: -6px;
    color: var(--numeral-dark);
  }
  .envelope .figure { left: 232px; top: 300px; width: 66px; height: 140px; }
  .envelope .org-name {
    position: absolute; left: 115px; top: 448px; width: 360px;
    font-size: 22px; line-height: 1.2; text-transform: uppercase;
    color: var(--harbor-blue); letter-spacing: .5px;
    display: flex; align-items: center; gap: 12px;
  }
  .envelope .org-name .mark {
    flex: none; width: 22px; height: 22px; background: var(--harbor-blue);
  }

  /* Invitation */
  .invite {
    position: absolute; left: 696px; top: 91px;
    width: 464px; height: 630px; overflow: hidden;
    color: var(--paper-white);
  }
  .invite .numeral {
    position: absolute; right: 8px; top: -30px;
    font-size: 180px; line-height: 1; letter-spacing: -5px;
    color: var(--bright-blue);
  }
  .invite .org-mark {
    position: absolute; left: 22px; top: 18px;
    font-size: 10px; line-height: 1.25; text-transform: uppercase; width: 130px;
    color: var(--paper-white);
  }
  .invite .title {
    position: absolute; left: 22px; top: 70px;
    font-size: 22px; font-weight: 400; letter-spacing: .3px;
    color: var(--paper-white);
  }
  .invite .details {
    position: absolute; right: 20px; top: 312px; text-align: right;
    font-size: 16px; line-height: 36px; color: var(--paper-white);
  }
  .invite .rsvp {
    position: absolute; left: 22px; top: 448px;
    font-size: 14px; line-height: 28px; color: var(--bright-blue);
  }
  .invite .figure-reader { left: 26px; top: 575px; width: 40px; height: 50px; }
  .invite .figure-tumbler { left: 352px; top: 536px; width: 96px; height: 88px; }

  .caption { position: absolute; font-size: 19px; color: var(--label); }
  .caption-envelope { left: 38px; top: 752px; }
  .caption-invite { left: 716px; top: 728px; }
</style>
</head>
<body>
<main class="sheet">

  <section class="envelope streaks" aria-label="Back side of envelope">
    <svg class="flap" viewBox="0 0 590 350" preserveAspectRatio="none" aria-hidden="true">
      <defs>
        <linearGradient id="flapBlue" x1="0" y1="0" x2="0" y2="1">
          <stop offset="0" stop-color="#4aa6e6"/>
          <stop offset="1" stop-color="#1f6fb0"/>
        </linearGradient>
      </defs>
      <polygon points="0,0 590,0 590,204 295,336 0,204" fill="url(#flapBlue)"/>
    </svg>
    <div class="numeral">35</div>
    <div class="placeholder-figure figure" role="img" aria-label="Blue silhouette of a child kicking a ball"></div>
    <p class="org-name"><span class="mark" aria-hidden="true"></span><span>Tarnwick Youth<br>Harbor Centers</span></p>
  </section>

  <section class="invite streaks" aria-label="Invitation">
    <div class="numeral">35</div>
    <p class="org-mark">Tarnwick Youth<br>Harbor Centers</p>
    <h1 class="title">Annual Benefit Gala</h1>
    <div class="details">
      <p>Marlowe Hall Club of Chicago</p>
      <p>Saturday, November 3, 2012</p>
    </div>
    <div class="rsvp">
      <p>Please respond by October 26, 2012</p>
      <p>MHC Overnight Package Available Black Tie Preferred</p>
    </div>
    <div class="placeholder-figure figure-reader" role="img" aria-label="Blue silhouette of a seated child reading"></div>
    <div class="placeholder-figure figure-tumbler" role="img" aria-label="Blue silhouette of a child doing a cartwheel"></div>
  </section>

  <p class="caption caption-envelope">back side of envelope</p>
  <p class="caption caption-invite">invite</p>

</main>
</body>
</html>
```